Marlowick community hall home page

We are building a modern, responsive website & booking system for our community hall. For this PixelForge task, we would like to receive design ideas for the home page.
There are no limits on the colours or fonts that can be used. We are looking for a modern, fresh design with a local/community feel. We don’t have a logo but we also recognise that our name is quite long! … So initials (MCH) instead of the name would be fine.
People book our community hall for a range of activities including: fitness classes, wedding receptions, birthday parties, business meetings, teaching, community events, charity fundraisers and other celebrations.
We have three main goals for the website. The first is that people can check our calendar and make a booking for an available time slot. The second is that they can read about our facilities and the prices for hiring them. The third is that people can find out about upcoming activities & events.
CTA: Book now
A button that links to a booking request form. (The form is not part of this design project)
Primary/Header navigation:
Home | Calendar | Facilities | Prices | Photos | News | Contact
Secondary/Footer navigation:
Chatterleaf | Quillcast
Login | Register | Privacy policy | Terms & conditions
Example texts (lorem ipsum etc. is also fine):
We have everything you need from a venue, whether it’s an elegant room with ample flexible space, a lavish and elegant hall for a wedding reception, a conference room that fits 125 delegates or a easy access venue to the town centre.
The hall is available for hire for wedding receptions, birthday celebrations, anniversaries, children's parties, presentations, lectures, fitness groups, and will comfortably accommodate all your guests.
This venue is well equipped with a modern kitchen, a range of audio and technical services, hearing loop, licensed bar, conference facilities, disabled access and unlimited free WiFi.
You can use this website to find out more about our rooms, equipment and the services we can offer and use the calendar to see where we have rooms available. You can also book rooms using our online booking system.
To the front of the building is a large public open grassed area across which is a row of shops. To the rear of the building is the large car park, including spaces for blue badge holders and a large enclosed cycle rack. This area also has extensive gardens, with seating and planting areas maintained by local volunteers.
The community hall is run and managed by volunteers of the Marlowick Community Organisation. Our objectives are to increase opportunities for people living in and around Pepperton.
We are passionate about being the heart of the community; caring for this community centred property and visitors are at the heart of all we do.
Where to go next
— Check when the hall is free
— Read our booking policy documents
— Make a booking reservation
Amenities
— Free WiFi
— Free car parking
— Fully equipped kitchen
— Hearing loop
Details for our most popular facilities (rooms):
Name: Main hall
Short description: A 127 square metre main hall with entrance lobby, toilets, a well-equipped kitchen and separate storage facilities. Three sets of double doors provide access to a large paved area and the adjacent playing field.
Capacity: 180 people
Price: £10-20 per hour
Links: More info | Book now
Name: Large meeting room
Short description: A delightful, spacious room with an outlook and access to the small walled garden. Ideal for meetings and small gatherings - it has its own access door and the use of a disabled W/C. We offer a reduced rate for this room when booked together with the main hall.
Capacity: 20 people
Price: £6-12 per hour
Attachments:
We have attached some photos of the hall & some (royalty free) stock images for inspiration.

```html
<!DOCTYPE html>
<html lang="en">
<head>
<meta charset="utf-8">
<title>Marlowick Community Hall</title>
<link href="https://fonts.googleapis.com/css2?family=Montserrat:wght@300;400;500;600;700&display=swap" rel="stylesheet">
<style>
:root{
  --ink:#1d1d24;
  --body:#4a4a52;
  --purple:#a56cd6;
  --pink:#f43d7c;
  --teal:#55d6bd;
  --yellow:#fdb93a;
  --blue:#2aa6d6;
  --green:#8dd04a;
  --lavender:#b88be3;
  --gallery-bg:#f0f3f3;
  --white:#ffffff;
}
*{margin:0;padding:0;box-sizing:border-box}
html,body{width:1200px;height:4515px;overflow:hidden}
body{position:relative;font-family:'Montserrat',sans-serif;color:var(--ink);background:var(--white)}
.abs{position:absolute}
.img{position:absolute;display:block}

/* header & hero */
.hero{left:0;top:0;width:1200px;height:690px;background:linear-gradient(180deg,#3a2c22 0%,#5b4a3c 45%,#6e5e50 70%,#4a3c30 100%)}
.logo{left:110px;top:22px;font-size:32px;font-weight:700;color:var(--white);letter-spacing:3px}
.nav a{position:absolute;top:31px;font-size:12px;color:var(--white);text-decoration:none;letter-spacing:.5px;font-weight:400}
.nav a.current{font-weight:700}
.btn-contact{left:1011px;top:21px;width:128px;height:35px;border-radius:18px;background:var(--yellow);color:var(--white);font-size:12px;font-weight:600;text-align:center;line-height:35px;letter-spacing:.5px}
.hero-box{left:340px;top:235px;width:520px;height:206px;border:2px solid rgba(255,255,255,.75);background:rgba(30,24,20,.45)}
.hero-title{left:340px;top:270px;width:520px;text-align:center;color:var(--white);font-size:44px;line-height:50px;letter-spacing:1px}
.hero-title b{font-weight:600;display:block}
.hero-title span{font-weight:300;display:block}
.btn-book-hero{left:532px;top:377px;width:137px;height:32px;border-radius:16px;background:var(--pink);color:var(--white);font-size:10px;font-weight:600;letter-spacing:2px;text-align:center;line-height:32px}
.dot{top:582px;width:16px;height:16px;border-radius:50%;background:var(--white)}
.dot.active{background:#1b1b1b}

/* feature circles */
.feature{width:318px;height:318px;border-radius:50%;color:var(--white);text-align:center}
.feature.teal{background:radial-gradient(circle at 60% 40%,#7fe3d0,#4fd1b8)}
.feature.pink{background:radial-gradient(circle at 60% 40%,#ff5c95,#f22c72)}
.feature.yellow{background:radial-gradient(circle at 60% 40%,#ffd15c,#fdb33a)}
.feature .icon{position:absolute;left:123px;top:44px;width:72px;height:72px;border-radius:50%;background:var(--white)}
.feature h3{position:absolute;left:0;width:318px;font-size:18px;font-weight:700;line-height:22px;letter-spacing:.5px}
.feature .pill{position:absolute;left:91px;width:136px;height:34px;border:2px solid var(--white);border-radius:17px;font-size:10px;font-weight:600;letter-spacing:2px;line-height:30px}

/* about */
.about-frame{left:84px;top:1037px;width:484px;height:461px;border:3px solid var(--yellow)}
.about-h{left:669px;top:1087px;font-size:33px;font-weight:700;line-height:40px;letter-spacing:.5px}
.rule{height:3px;width:70px;background:var(--purple)}
.about-p{left:669px;font-size:13px;line-height:25px;color:var(--body);width:460px}
.btn-outline{border:2px solid var(--pink);border-radius:22px;color:var(--pink);font-size:10px;font-weight:600;letter-spacing:2px;text-align:center}

/* section headings */
.section-h{left:0;width:1200px;text-align:center;font-size:31px;font-weight:700;letter-spacing:1px}

/* facilities */
.facilities{left:0;top:1649px;width:1200px;height:679px;background:linear-gradient(90deg,#f1e3f6 0%,#f9e6ef 100%)}
.tile{width:252px;height:213px}
.tile .label{position:absolute;left:6px;right:6px;bottom:7px;height:42px;color:var(--white);font-size:12px;font-weight:600;text-align:center;line-height:42px;letter-spacing:.3px}

/* activities */
.card{width:324px;height:442px;border:1px solid #d9d9de;background:var(--white)}
.card h4{position:absolute;left:38px;top:260px;font-size:17px;font-weight:600}
.card p{position:absolute;left:38px;top:296px;width:250px;font-size:10.5px;line-height:18.5px;color:var(--body)}
.card .btn-outline{position:absolute;left:35px;top:378px;width:124px;height:32px;line-height:28px;font-size:8.5px}

/* gallery */
.gallery{left:0;top:3013px;width:1200px;height:771px;background:var(--gallery-bg)}

/* booking */
.booking{left:0;top:3784px;width:1200px;height:514px;background:linear-gradient(100deg,#ffbf3a 0%,#fd9b45 40%,#f86a66 70%,#f5437c 100%)}
.booking-h{left:0;top:3830px;width:1200px;text-align:center;color:var(--white);font-size:31px;font-weight:300;letter-spacing:2px}
.field{background:var(--white);border-radius:24px;font-size:11px;color:#444;padding-left:22px;line-height:48px}
.field i{color:var(--pink);font-style:normal}
.btn-submit{left:517px;top:4198px;width:166px;height:39px;border-radius:20px;background:#3a0a22;color:var(--white);font-size:11px;font-weight:600;letter-spacing:2px;text-align:center;line-height:39px}

/* footer */
.foot-nav a{position:absolute;top:4346px;font-size:12px;color:var(--ink);text-decoration:none;font-weight:500}
.foot-line{left:0;top:4389px;width:1200px;height:1px;background:#e3e3e6}
.foot-links{left:0;top:4412px;width:1200px;text-align:center;font-size:10px;color:#333}
.social{top:4446px;display:flex;align-items:center;gap:6px;font-size:11px;font-weight:500;color:var(--ink)}
.social span.c{width:14px;height:14px;border-radius:50%;background:var(--pink)}
</style>
</head>
<body>

<!-- Header / hero -->
<div class="hero abs" role="img" aria-label="Photo of an elegant banquet hall with round tables, white cloths and a chandelier"></div>
<div class="logo abs">MCH</div>
<nav class="nav">
  <a class="current" style="left:388px">HOME</a>
  <a style="left:482px">CALENDAR</a>
  <a style="left:608px">FACILITIES</a>
  <a style="left:731px">PRICES</a>
  <a style="left:832px">PHOTOS</a>
  <a style="left:941px">NEWS</a>
</nav>
<div class="btn-contact abs">CONTACT</div>
<div class="hero-box abs"></div>
<h1 class="hero-title abs"><b>MARLOWICK</b><span>COMMUNITY HALL</span></h1>
<div class="btn-book-hero abs">BOOK NOW</div>
<div class="dot active abs" style="left:561px"></div>
<div class="dot abs" style="left:603px"></div>
<div class="dot abs" style="left:644px"></div>

<!-- Feature circles -->
<div class="feature teal abs" style="left:127px;top:633px">
  <div class="icon">
    <svg width="72" height="72" viewBox="0 0 72 72" fill="none" stroke="#4fd1b8" stroke-width="2" stroke-linecap="round">
      <path d="M36 52V30M36 30l-6-6M36 30l6-6M36 24v-6M26 50l-4-12M46 50l4-12M22 38l-4-4M50 38l4-4"/>
      <circle cx="36" cy="16" r="2"/><circle cx="18" cy="32" r="2"/><circle cx="54" cy="32" r="2"/>
    </svg>
  </div>
  <h3 style="top:147px">FACILITIES<br>PROVIDES</h3>
  <div class="pill" style="top:204px">LEARN MORE</div>
</div>
<div class="feature pink abs" style="left:459px;top:633px">
  <div class="icon">
    <svg width="72" height="72" viewBox="0 0 72 72" fill="none" stroke="#f22c72" stroke-width="2" stroke-linecap="round">
      <rect x="20" y="20" width="32" height="22" rx="2"/><path d="M32 42v6M40 42v6M26 50h20M26 28h14M26 34h10"/>
      <path d="M44 30l3 3 5-6"/>
    </svg>
  </div>
  <h3 style="top:147px">MAKE A<br>BOOKING NOW</h3>
  <div class="pill" style="top:204px">BOOK NOW</div>
</div>
<div class="feature yellow abs" style="left:791px;top:641px">
  <div class="icon">
    <svg width="72" height="72" viewBox="0 0 72 72" fill="none" stroke="#fdb33a" stroke-width="2" stroke-linecap="round">
      <path d="M18 40h36M22 40v12M50 40v12M28 40V28M36 40V24M44 40V28"/><circle cx="28" cy="25" r="2"/><circle cx="36" cy="21" r="2"/><circle cx="44" cy="25" r="2"/>
    </svg>
  </div>
  <h3 style="top:147px">ACTIVITIES &amp;<br>EVENTS</h3>
  <div class="pill" style="top:204px">VIEW EVENTS</div>
</div>

<!-- About -->
<div class="about-frame abs"></div>
<div class="img" style="left:103px;top:1053px;width:447px;height:422px;background:linear-gradient(160deg,#2a2a7a 0%,#7a3fbf 40%,#4a3560 70%,#2a2230 100%)" role="img" aria-label="Photo of guests seated at tables in the hall under purple lighting"></div>
<div class="img" style="left:350px;top:1327px;width:253px;height:231px;background:var(--white)"></div>
<div class="img" style="left:356px;top:1333px;width:241px;height:219px;background:linear-gradient(160deg,#e9e4da,#c9c0b0 60%,#a99f8c)" role="img" aria-label="Photo of a white flower centrepiece on a dressed reception table"></div>
<h2 class="about-h abs">ABOUT MARLOWICK<br>COMMUNITY HALL</h2>
<div class="rule abs" style="left:669px;top:1174px"></div>
<p class="about-p abs" style="top:1214px">Lorem Ipsum is simply dummy text of the printing and typesetting industry. Lorem Ipsum has been the industry's standard dummy text ever since the 1500s, when an unknown printer took a galley of type and scrambled it to make a type specimen book.</p>
<p class="about-p abs" style="top:1327px">It has survived not only five centuries, but also the leap into electronic typesetting, remaining essentially unchanged.</p>
<div class="btn-outline abs" style="left:669px;top:1423px;width:158px;height:40px;line-height:36px">LEARN MORE</div>

<!-- Facilities -->
<div class="facilities abs"></div>
<h2 class="section-h abs" style="top:1716px">FACILITIES PROVIDES</h2>
<div class="rule abs" style="left:565px;top:1765px"></div>

<div class="tile abs" style="left:72px;top:1805px;background:linear-gradient(150deg,#f3d9c9,#d9a88e)" role="img" aria-label="Photo of wedding reception flowers"><div class="label" style="background:var(--pink)">WEDDING RECEPTIONS</div></div>
<div class="tile abs" style="left:342px;top:1805px;background:linear-gradient(150deg,#cfe7ef,#e8b97a)" role="img" aria-label="Photo of a birthday buffet table"><div class="label" style="background:var(--yellow)">BIRTHDAY CELEBRATIONS</div></div>
<div class="tile abs" style="left:610px;top:1805px;background:linear-gradient(150deg,#d9d6cf,#8c857a)" role="img" aria-label="Photo of a dining room set for an anniversary"><div class="label" style="background:var(--teal)">ANNIVERSARIES</div></div>
<div class="tile abs" style="left:878px;top:1805px;background:linear-gradient(160deg,#dfe6ec 0%,#d9c45a 60%,#e0b630)" role="img" aria-label="Photo of children playing on a bouncy castle"><div class="label" style="background:var(--lavender)">CHILDREN'S PARTIES</div></div>

<div class="tile abs" style="left:72px;top:2036px;background:linear-gradient(150deg,#c9c6c1,#8c8270)" role="img" aria-label="Photo of a meeting room with a screen for presentations"><div class="label" style="background:var(--lavender)">PRESENTATIONS</div></div>
<div class="tile abs" style="left:342px;top:2036px;background:linear-gradient(150deg,#2c4a7a,#c04a3a 50%,#e0a030)" role="img" aria-label="Photo of a stained glass window"><div class="label" style="background:var(--pink)">LECTURES</div></div>
<div class="tile abs" style="left:610px;top:2036px;background:linear-gradient(150deg,#f4f4f4,#d8d4d0)" role="img" aria-label="Photo of a yoga session"><div class="label" style="background:var(--green)">FITNESS GROUPS</div></div>
<div class="tile abs" style="left:878px;top:2036px;background:linear-gradient(150deg,#3aa6d8,#1b4a8a 60%,#14203a)" role="img" aria-label="Photo of a large crowd at an event"><div class="label" style="background:var(--blue)">ACCOMMODATE GUESTS</div></div>

<!-- Activities & events -->
<h2 class="section-h abs" style="top:2404px">ACTIVITIES &amp; EVENTS</h2>
<div class="rule abs" style="left:565px;top:2452px"></div>

<div class="card abs" style="left:98px;top:2500px">
  <div class="img" style="left:0;top:0;width:322px;height:233px;background:linear-gradient(160deg,#e8e6e2,#b9b2a6 60%,#6b645a)" role="img" aria-label="Photo of a meeting room with a long conference table"></div>
  <h4>Large meeting room</h4>
  <p>A delightful, spacious room with an outlook and access to the small walled garden. Ideal for meetings and small gatherings - it has its own access door and the use of a disabled \</p>
  <div class="btn-outline">LEARN MORE</div>
</div>
<div class="card abs" style="left:440px;top:2500px">
  <div class="img" style="left:0;top:0;width:322px;height:233px;background:linear-gradient(160deg,#2c3e7a,#c9a040 45%,#3a4a8a 75%,#e8e6f0)" role="img" aria-label="Photo of a hall set with tables below a stained glass window"></div>
  <h4>Large meeting room</h4>
  <p>A delightful, spacious room with an outlook and access to the small walled garden. Ideal for meetings and small gatherings - it has its own access door and the use of a disabled \</p>
  <div class="btn-outline">LEARN MORE</div>
</div>
<div class="card abs" style="left:776px;top:2500px">
  <div class="img" style="left:0;top:0;width:322px;height:233px;background:linear-gradient(160deg,#e9e4da,#c9c0b0 60%,#a99f8c)" role="img" aria-label="Photo of a white flower centrepiece on a reception table"></div>
  <h4>Large meeting room</h4>
  <p>A delightful, spacious room with an outlook and access to the small walled garden. Ideal for meetings and small gatherings - it has its own access door and the use of a disabled \</p>
  <div class="btn-outline">LEARN MORE</div>
</div>

<!-- Gallery -->
<div class="gallery abs"></div>
<h2 class="section-h abs" style="top:3060px">OUR GALLERY</h2>
<div class="rule abs" style="left:565px;top:3110px"></div>
<div class="img" style="left:117px;top:3155px;width:480px;height:235px;background:linear-gradient(150deg,#eae3da,#d3b08c 60%,#c49a6c)" role="img" aria-label="Photo of biscuits being iced"></div>
<div class="img" style="left:606px;top:3155px;width:480px;height:235px;background:linear-gradient(150deg,#e9e4da,#c9c0b0 60%,#a99f8c)" role="img" aria-label="Photo of a floral centrepiece in the hall"></div>
<div class="img" style="left:119px;top:3400px;width:317px;height:235px;background:linear-gradient(150deg,#2a3a2a,#7a3040 50%,#d8d0c8)" role="img" aria-label="Photo of flowers and glassware on a table"></div>
<div class="img" style="left:445px;top:3400px;width:317px;height:235px;background:linear-gradient(150deg,#3a1a5a,#8a2ab0 50%,#d08a40)" role="img" aria-label="Photo of a lantern centrepiece under purple lighting"></div>
<div class="img" style="left:769px;top:3400px;width:317px;height:235px;background:linear-gradient(160deg,#9cc4e4,#3a6a30 50%,#a04a30)" role="img" aria-label="Photo of the red brick hall building among trees"></div>
<div class="btn-outline abs" style="left:508px;top:3674px;width:196px;height:49px;line-height:45px;font-size:13px">VIEW MORE</div>

<!-- Booking form -->
<div class="booking abs"></div>
<h2 class="booking-h abs">BOOKING FORM</h2>
<div class="rule abs" style="left:565px;top:3889px;background:var(--white)"></div>
<div class="field abs" style="left:212px;top:3924px;width:385px;height:48px">First Name<i>*</i></div>
<div class="field abs" style="left:606px;top:3924px;width:386px;height:48px">Last Name<i>*</i></div>
<div class="field abs" style="left:212px;top:3986px;width:385px;height:47px">E-mail<i>*</i></div>
<div class="field abs" style="left:606px;top:3986px;width:386px;height:47px">Phone<i>*</i></div>
<div class="field abs" style="left:212px;top:4049px;width:780px;height:128px;border-radius:14px;line-height:40px;padding-left:26px">Leave us a message here</div>
<div class="btn-submit abs">BOOK NOW</div>

<!-- Footer -->
<nav class="foot-nav">
  <a style="left:212px">HOME</a>
  <a style="left:314px">CALENDAR</a>
  <a style="left:447px">FACILITIES</a>
  <a style="left:577px">PRICES</a>
  <a style="left:685px">PHOTOS</a>
  <a style="left:803px">NEWS</a>
  <a style="left:904px">CONTACT</a>
</nav>
<div class="foot-line abs"></div>
<div class="foot-links abs">Login &nbsp;|&nbsp; Register &nbsp;|&nbsp; Privacy policy &nbsp;|&nbsp; Terms &amp; conditions</div>
<div class="social abs" style="left:500px"><span class="c"></span>Chatterleaf</div>
<div class="social abs" style="left:622px"><span class="c"></span>Quillcast</div>

</body>
</html>
```